Revamp of existing namecard

Existingly, i've got a namecard that i would like to retain the main design. but there are some changes in my company and i would need to do some amendments to it.

We are a money transfer and money exchange company.
I need 2 different types of name card.
1. For individual name cards
the front to put the following:
Company name and logo
English Name, Chinese Name appointment
Mobile Number, Email and Website.
2 License number under the logo and name

the back of the name card to put
8 address: 7 Singapore and 1 Hong Kong branch addresses
8 Mobile Number of the corresponding addresses.

We would like to retain the name card front design
the name card back design can change but color to retain.

2nd name card is generic name card
Front:
Company name and logo
Branch Mobile Number, Branch Address, Email and Website.

Industry/Entity Type

remittance and money exchange

Contact Information for Business Card

I need 2 different types of name card. 1. For individual name cards the front to put the following: Company name and logo English Name, Chinese Name appointment Mobile Number, Email and Website. 2 License number under the logo and name the back of the name card to put 8 address: 7 Singapore and 1 Hong Kong branch addresses 8 Mobile Number of the corresponding addresses. We would like to retain the name card front design the name card back design can change but color to retain. 2nd name card is generic name card Front: the front to put the following: Company name and logo Branch Mobile Number, Branch Address, Email and Website. 2 License number under the logo and name

Requirements
Must have
• I need 2 different types of name card. 1. For individual name cards the front to put the following: Company name and logo English Name, Chinese Name appointment Mobile Number, Email and Website. 2 License number under the logo and name the back of the name card to put 8 address: 7 Singapore and 1 Hong Kong branch addresses 8 Mobile Number of the corresponding addresses. We would like to retain the name card front design the name card back design can change but color to retain. 2nd name card is generic name card Front: the front to put the following: Company name and logo Branch Mobile Number, Branch Address, Email and Website. 2 License number under the logo and name
Nice to have
• use back color code

```html
<!DOCTYPE html>
<html lang="en">
<head>
<meta charset="utf-8">
<title>Velora Name Cards</title>
<link href="https://fonts.googleapis.com/css2?family=Montserrat:wght@500;600;700&family=Noto+Sans+TC:wght@700&display=swap" rel="stylesheet">
<style>
  :root {
    --navy: #253340;
    --teal: #5cc4d5;
    --ink: #2a3441;
    --paper: #ffffff;
    --map-light: #f1f1f1;
    --map-mid: #e2e2e2;
    --backdrop: #ffffff;
  }
  * { margin: 0; padding: 0; box-sizing: border-box; }
  html, body { width: 1200px; height: 750px; overflow: hidden; background: var(--backdrop); }
  body { position: relative; font-family: "Montserrat", sans-serif; color: var(--ink); }

  .card {
    position: absolute; width: 530px; height: 303px; overflow: hidden;
    box-shadow: 6px 8px 10px rgba(0,0,0,0.28);
  }
  .card--front-personal { left: 38px; top: 42px; background: var(--paper); }
  .card--front-branch { left: 633px; top: 42px; background: var(--paper); }
  .card--back-branches { left: 38px; top: 411px; background: var(--navy); color: #fff; }
  .card--back-brand { left: 633px; top: 410px; background: var(--navy); }

  .world-map {
    position: absolute; left: 20px; top: 32px; width: 490px; height: 282px;
    background: radial-gradient(ellipse at 55% 40%, var(--map-mid) 0%, var(--map-light) 55%, rgba(255,255,255,0) 75%);
  }

  .brand {
    position: absolute; display: flex; align-items: center; gap: 9px;
    font-weight: 700; letter-spacing: 1px; line-height: 1;
  }
  .brand__dot { width: 30px; height: 30px; border-radius: 50%; background: var(--teal); flex: none; }
  .brand__name { font-size: 38px; color: var(--ink); }
  .card--front-personal .brand,
  .card--front-branch .brand { right: 32px; top: 33px; }

  .person { position: absolute; left: 31px; top: 94px; }
  .person__name { font-size: 22px; font-weight: 700; line-height: 26px; }
  .person__name-zh { font-family: "Noto Sans TC", sans-serif; font-size: 20px; font-weight: 700; line-height: 22px; letter-spacing: 1px; }
  .person__role { font-size: 14.5px; font-weight: 500; color: var(--teal); line-height: 22px; margin-top: 2px; }

  .contacts { position: absolute; list-style: none; font-size: 12.5px; font-weight: 500; }
  .contacts li { display: flex; align-items: center; gap: 10px; height: 21.5px; }
  .contacts svg { width: 12px; height: 14px; flex: none; }
  .contacts .phone { letter-spacing: 2.4px; }
  .card--front-personal .contacts { left: 31px; top: 180px; }
  .card--front-branch .contacts { left: 32px; top: 155px; }

  .address { position: absolute; left: 32px; top: 111px; font-size: 12.5px; font-weight: 500; line-height: 21px; }

  .licences { position: absolute; right: 34px; text-align: right; color: var(--teal); font-size: 14.5px; font-weight: 500; line-height: 21px; }
  .card--front-personal .licences { bottom: 24px; }
  .card--front-branch .licences { bottom: 24px; }

  .side-brand {
    position: absolute; left: 34px; top: 20px; width: 38px; height: 268px;
    display: flex; flex-direction: column; align-items: center; gap: 12px;
  }
  .side-brand__name {
    writing-mode: vertical-rl; transform: rotate(180deg);
    font-size: 34px; font-weight: 700; letter-spacing: 1px; color: #fff; line-height: 1;
  }
  .side-brand__dot { width: 34px; height: 34px; border-radius: 50%; background: var(--teal); }

  .branches { position: absolute; left: 117px; top: 22px; }
  .branches__region { font-size: 14px; font-weight: 600; color: var(--teal); line-height: 18px; margin-bottom: 3px; }
  .branches__region--hk { margin-top: 12px; margin-bottom: 6px; }
  .branch { font-size: 10.3px; font-weight: 500; line-height: 12.6px; position: relative; }
  .branch__phone { position: relative; }
  .branch__phone svg { position: absolute; left: -17px; top: 0; width: 11px; height: 11px; }

  .brand--center { left: 135px; top: 136px; }
  .brand--center .brand__name { color: #fff; font-size: 36px; }
  .tagline { position: absolute; right: 137px; top: 172px; font-size: 12.5px; font-weight: 500; color: var(--teal); }
</style>
</head>
<body>

<!-- Personal card, front -->
<section class="card card--front-personal">
  <div class="world-map" role="img" aria-label="Dotted world map in light grey"></div>
  <div class="brand"><span class="brand__dot"></span><span class="brand__name">VELORA</span></div>
  <div class="person">
    <p class="person__name">Marcus Lim</p>
    <p class="person__name-zh">林志明</p>
    <p class="person__role">Director of Business Development</p>
  </div>
  <ul class="contacts">
    <li class="phone"><svg viewBox="0 0 12 16"><rect x="2" y="0.8" width="8" height="14.4" rx="1.6" fill="none" stroke="#5cc4d5" stroke-width="1.4"/><circle cx="6" cy="12.8" r="0.9" fill="#5cc4d5"/></svg>+852 9412 3087</li>
    <li><svg viewBox="0 0 14 12"><rect x="0.5" y="1.5" width="13" height="9" fill="#5cc4d5"/><path d="M0.5 1.5 L7 7 L13.5 1.5" fill="none" stroke="#fff" stroke-width="1"/></svg>marcus@velora.com.hk</li>
    <li><svg viewBox="0 0 14 14"><circle cx="7" cy="7" r="6" fill="none" stroke="#5cc4d5" stroke-width="1.2"/><ellipse cx="7" cy="7" rx="2.6" ry="6" fill="none" stroke="#5cc4d5" stroke-width="1"/><path d="M1 7 H13 M2 4 H12 M2 10 H12" stroke="#5cc4d5" stroke-width="0.9"/></svg>www.velora.com.hk</li>
  </ul>
  <p class="licences">81402257-000-04-19-A</p>
</section>

<!-- Branch card, front -->
<section class="card card--front-branch">
  <div class="world-map" role="img" aria-label="Dotted world map in light grey"></div>
  <div class="brand"><span class="brand__dot"></span><span class="brand__name">VELORA</span></div>
  <p class="address">Unit 1807, 18th Floor, Harbour Crest Tower,<br>52 Lockhart Lane, Causeway Bay</p>
  <ul class="contacts">
    <li class="phone"><svg viewBox="0 0 12 16"><rect x="2" y="0.8" width="8" height="14.4" rx="1.6" fill="none" stroke="#5cc4d5" stroke-width="1.4"/><circle cx="6" cy="12.8" r="0.9" fill="#5cc4d5"/></svg>+852 9412 3087</li>
    <li><svg viewBox="0 0 14 12"><rect x="0.5" y="1.5" width="13" height="9" fill="#5cc4d5"/><path d="M0.5 1.5 L7 7 L13.5 1.5" fill="none" stroke="#fff" stroke-width="1"/></svg>marcus@velora.com.hk</li>
    <li><svg viewBox="0 0 14 14"><circle cx="7" cy="7" r="6" fill="none" stroke="#5cc4d5" stroke-width="1.2"/><ellipse cx="7" cy="7" rx="2.6" ry="6" fill="none" stroke="#5cc4d5" stroke-width="1"/><path d="M1 7 H13 M2 4 H12 M2 10 H12" stroke="#5cc4d5" stroke-width="0.9"/></svg>www.velora.com.hk</li>
  </ul>
  <p class="licences">81402257-000-04-19-A<br>86015534-000-04-21-B</p>
</section>

<!-- Personal card, back: branch list -->
<section class="card card--back-branches">
  <div class="side-brand"><span class="side-brand__name">VELORA</span><span class="side-brand__dot"></span></div>
  <div class="branches">
    <h2 class="branches__region">SINGAPORE</h2>
    <p class="branch">3 Anson Quay, Tower A, #21-04, 049211</p>
    <p class="branch branch__phone"><svg viewBox="0 0 12 12"><path d="M2.3 0.6 L4.3 2.9 L3.2 4.4 Q4.6 7.2 7.6 8.8 L9.1 7.7 L11.4 9.7 L9.9 11.4 Q4.6 11 0.6 2.1 Z" fill="#5cc4d5"/></svg>+65 6240 1183</p>
    <p class="branch">12 Bayfront Crescent, #30-02, 018766</p>
    <p class="branch branch__phone"><svg viewBox="0 0 12 12"><path d="M2.3 0.6 L4.3 2.9 L3.2 4.4 Q4.6 7.2 7.6 8.8 L9.1 7.7 L11.4 9.7 L9.9 11.4 Q4.6 11 0.6 2.1 Z" fill="#5cc4d5"/></svg>+65 6591 2074</p>
    <p class="branch">5 Cecil Walk, Orion Tower, #16-09, 069533</p>
    <p class="branch branch__phone"><svg viewBox="0 0 12 12"><path d="M2.3 0.6 L4.3 2.9 L3.2 4.4 Q4.6 7.2 7.6 8.8 L9.1 7.7 L11.4 9.7 L9.9 11.4 Q4.6 11 0.6 2.1 Z" fill="#5cc4d5"/></svg>+65 9184 6620</p>
    <p class="branch">9 Telok Road, Meridian Finance Building, #19-06, 048207</p>
    <p class="branch branch__phone"><svg viewBox="0 0 12 12"><path d="M2.3 0.6 L4.3 2.9 L3.2 4.4 Q4.6 7.2 7.6 8.8 L9.1 7.7 L11.4 9.7 L9.9 11.4 Q4.6 11 0.6 2.1 Z" fill="#5cc4d5"/></svg>+65 9327 5508</p>
    <p class="branch">4 Seaview Avenue, Coral Bay Tower, #12-07, 098415</p>
    <p class="branch branch__phone"><svg viewBox="0 0 12 12"><path d="M2.3 0.6 L4.3 2.9 L3.2 4.4 Q4.6 7.2 7.6 8.8 L9.1 7.7 L11.4 9.7 L9.9 11.4 Q4.6 11 0.6 2.1 Z" fill="#5cc4d5"/></svg>+65 6613 7742</p>
    <p class="branch">66 Palmer Street, #20-03, 068511</p>
    <p class="branch branch__phone"><svg viewBox="0 0 12 12"><path d="M2.3 0.6 L4.3 2.9 L3.2 4.4 Q4.6 7.2 7.6 8.8 L9.1 7.7 L11.4 9.7 L9.9 11.4 Q4.6 11 0.6 2.1 Z" fill="#5cc4d5"/></svg>+65 8725 3096</p>
    <p class="branch">140 Novena Lane, Crescent Square, #14-05, 307712</p>
    <p class="branch branch__phone"><svg viewBox="0 0 12 12"><path d="M2.3 0.6 L4.3 2.9 L3.2 4.4 Q4.6 7.2 7.6 8.8 L9.1 7.7 L11.4 9.7 L9.9 11.4 Q4.6 11 0.6 2.1 Z" fill="#5cc4d5"/></svg>+65 8346 0917</p>

    <h2 class="branches__region branches__region--hk">HONG KONG</h2>
    <p class="branch">Unit 1807, 18th Floor, Harbour Crest Tower, 52 Lockhart Lane, Causeway Bay</p>
    <p class="branch branch__phone"><svg viewBox="0 0 12 12"><path d="M2.3 0.6 L4.3 2.9 L3.2 4.4 Q4.6 7.2 7.6 8.8 L9.1 7.7 L11.4 9.7 L9.9 11.4 Q4.6 11 0.6 2.1 Z" fill="#5cc4d5"/></svg>+852 9730 4128</p>
  </div>
</section>

<!-- Branch card, back: brand panel -->
<section class="card card--back-brand" role="img" aria-label="Navy background with a repeating pattern of the brand symbol">
  <div class="brand brand--center"><span class="brand__dot"></span><span class="brand__name">VELORA</span></div>
  <p class="tagline">Remittance and Money Exchange</p>
</section>

</body>
</html>
```